Dune Air & Plus business card

I need an awesome, double-sided business card designed with our new logo. I would like the one side black with the colored logo, and the back side is all yours. I'd like to see horizontal and vertical layouts. Get creative! Thank you.

Target Market(s)

HVAC, Heating and Cooling in Phoenix, AZ

Industry/Entity Type

HVAC

Contact Information for Business Card

We need our new logo on the card. Tom Harker, (623) 555-0142, tom@trydunesair.com, www.trydunesair.com, ROC 514273

```html
<!DOCTYPE html>
<html lang="en">
<head>
<meta charset="utf-8">
<title>Dune Air &amp; Plus – Business Card</title>
<link href="https://fonts.googleapis.com/css2?family=Arimo:wght@400;700&display=swap" rel="stylesheet">
<style>
  :root {
    --backdrop: #161616;
    --card: #262626;
    --ink: #ffffff;
    --accent-orange: #f0701e;
    --accent-red: #df2a26;
    --accent-amber: #f6a124;
    --accent-blue: #1f78d1;
  }
  * { margin: 0; padding: 0; box-sizing: border-box; }
  html, body {
    width: 1200px; height: 900px; overflow: hidden;
    background: var(--backdrop);
    font-family: "Arimo", Arial, sans-serif;
  }
  .canvas { position: relative; width: 1200px; height: 900px; }
  .card {
    position: absolute; left: 250px;
    width: 700px; height: 400px;
    background: var(--card);
    overflow: hidden;
    box-shadow: 0 10px 30px rgba(0,0,0,.5);
  }
  .card--front { top: 40px; }
  .card--back { top: 465px; }

  .holder-name {
    position: absolute; left: 60px; top: 48px;
    color: var(--accent-orange);
    font-weight: 700; font-size: 36px; letter-spacing: .5px;
    text-transform: uppercase;
  }
  .holder-title {
    position: absolute; left: 60px; top: 92px;
    color: var(--ink); font-size: 21px;
  }
  .divider {
    position: absolute; left: 60px; top: 138px;
    width: 590px; height: 1px;
    background: linear-gradient(90deg, var(--accent-red), var(--accent-amber));
  }
  .contact-list {
    position: absolute; left: 60px; top: 162px;
    list-style: none;
  }
  .contact-item {
    display: flex; align-items: center; gap: 12px;
    color: var(--ink); font-size: 19px; line-height: 34px;
  }
  .contact-icon { width: 16px; height: 16px; flex: none; }

  .brand-wordmark {
    position: absolute;
    display: flex; align-items: center; gap: 12px;
    color: var(--accent-blue);
    font-weight: 700;
  }
  .card--front .brand-wordmark { right: 60px; top: 205px; font-size: 30px; }
  .brand-dot {
    display: inline-block; border-radius: 50%;
    background: var(--accent-orange);
  }
  .card--front .brand-dot { width: 22px; height: 22px; }

  .license {
    position: absolute; right: 60px; bottom: 40px;
    color: var(--ink); font-size: 20px;
  }
  .accent-band {
    position: absolute; left: 0; bottom: 0;
    width: 100%; height: 10px;
    background: linear-gradient(90deg, var(--accent-red), var(--accent-orange) 55%, var(--accent-amber));
  }

  .card--back .brand-wordmark {
    left: 50%; top: 50%; transform: translate(-50%, -50%);
    font-size: 50px; white-space: nowrap;
  }
  .card--back .brand-dot { width: 34px; height: 34px; }
</style>
</head>
<body>
<main class="canvas">

  <section class="card card--front" aria-label="Card front with contact details">
    <h1 class="holder-name">Tom Harker</h1>
    <p class="holder-title">CEO/Founder</p>
    <div class="divider"></div>

    <ul class="contact-list">
      <li class="contact-item">
        <svg class="contact-icon" viewBox="0 0 16 16" aria-hidden="true">
          <path d="M4 1 L6.5 4.5 L5 6 C6 8.5 7.5 10 10 11 L11.5 9.5 L15 12 L13 15 C7 14.5 1.5 9 1 3 Z" fill="var(--accent-blue)"/>
        </svg>
        <span>(623) 555-0142</span>
      </li>
      <li class="contact-item">
        <svg class="contact-icon" viewBox="0 0 16 16" aria-hidden="true">
          <rect x="1" y="3" width="14" height="10" fill="var(--accent-blue)"/>
          <path d="M1 3 L8 9 L15 3" fill="none" stroke="var(--card)" stroke-width="1.3"/>
        </svg>
        <span>tom@trydunesair.com</span>
      </li>
      <li class="contact-item">
        <svg class="contact-icon" viewBox="0 0 16 16" aria-hidden="true">
          <circle cx="8" cy="8" r="7" fill="var(--accent-blue)"/>
          <path d="M1 8 H15 M8 1 C5 4 5 12 8 15 M8 1 C11 4 11 12 8 15" fill="none" stroke="var(--card)" stroke-width="1"/>
        </svg>
        <span>www.trydunesair.com</span>
      </li>
    </ul>

    <div class="brand-wordmark"><span class="brand-dot"></span>Dune Air &amp; Plus</div>

    <p class="license">ROC 514273</p>
    <div class="accent-band"></div>
  </section>

  <section class="card card--back" aria-label="Card back with brand name">
    <div class="brand-wordmark"><span class="brand-dot"></span>Dune Air &amp; Plus</div>
  </section>

</main>
</body>
</html>
```